Medical Device Company needs website

We are a start-up medical device company looking to sell boot (foot) and brace (ankle) products on Shopify. We are still working on the name but you can use Kaltir as a placeholder- no logo yet)

Website information:
- Look: modern/tech with clean lines and symmetry.
- Colors: teal, white, black, and greys.
- Headers: home, shop, about us, help, blog
- Icons (upper right): search, my account and shopping cart
-place to sign up for newsletter

```html
<!DOCTYPE html>
<html lang="en">
<head>
<meta charset="UTF-8">
<title>Kaltir – Home</title>
<link rel="stylesheet" href="https://fonts.googleapis.com/css2?family=Outfit:wght@400;500;600;700&display=swap">
<style>
:root{
  --teal-900:#0b4a47;
  --teal-800:#0d5d59;
  --teal-700:#0f6e69;
  --teal-500:#2a9d96;
  --teal-200:#bfe6e2;
  --teal-100:#dcf1ef;
  --grey-50:#f7f7f8;
  --grey-100:#eceef0;
  --grey-400:#9aa3a3;
  --ink:#1d2625;
  --white:#ffffff;
  --sale:#8cc56a;
  --sold:#e8b82a;
}
*{box-sizing:border-box;margin:0;padding:0}
html,body{width:1200px;height:2650px;overflow:hidden;background:var(--grey-100);font-family:"Outfit",sans-serif;color:var(--ink)}
.page{position:absolute;left:0;top:192px;width:1200px;height:2265px;background:var(--white);overflow:hidden}
.abs{position:absolute}

/* top bar */
.topbar{left:0;top:0;width:1200px;height:31px;background:var(--teal-700);color:#cfe9e6;font-size:10px;line-height:31px;padding-left:157px}
.topbar a{color:#cfe9e6}
.topbar-icons{position:absolute;right:157px;top:7px;display:flex;gap:12px}

/* hero */
.hero{left:0;top:31px;width:1200px;height:536px;background:radial-gradient(ellipse at 78% 40%,#a9ddd8 0,#c3e7e3 35%,transparent 60%),linear-gradient(160deg,#cdeae7 0%,#bfe5e1 45%,#d7efed 100%)}
.logo{left:157px;top:44px;font-size:25px;font-weight:600;color:var(--teal-900)}
.nav{left:461px;top:54px;display:flex;gap:30px;font-size:11px;color:var(--ink)}
.nav .active{color:var(--teal-700);text-decoration:underline}
.search{left:862px;top:50px;width:181px;border-bottom:1px solid #b3d6d2;padding:0 0 6px 20px;font-size:11px;color:var(--teal-500)}
.search svg{position:absolute;left:2px;top:1px}
.eyebrow{left:157px;top:204px;font-size:15px;font-weight:500;color:var(--teal-900)}
.hero-title{left:157px;top:232px;font-size:45px;line-height:52px;font-weight:700;color:var(--teal-900);letter-spacing:.3px}
.btn-light{background:var(--white);color:var(--ink);font-size:11px;text-align:center;border-radius:2px}
.hero-btn{left:157px;top:352px;width:90px;height:31px;line-height:31px}
.hero-img{left:658px;top:125px;width:358px;height:339px;border-radius:40% 45% 35% 40%;background:radial-gradient(ellipse at 40% 45%,#7d8688 0,#b7c9cb 40%,#d9f0ee 75%,transparent 76%)}
.dots{left:572px;top:536px;display:flex;gap:7px}
.dots span{width:10px;height:10px;border:1px solid var(--teal-500);border-radius:50%}
.dots .on{background:radial-gradient(circle,var(--teal-700) 35%,transparent 40%)}

/* features */
.feature{top:612px;display:flex;gap:12px;align-items:center;font-size:12px}
.feature b{display:block;font-weight:600;color:var(--teal-900)}

/* grey band */
.band{left:0;top:866px;width:1200px;height:571px;background:var(--grey-50)}
.cat{top:718px;width:342px;height:185px;background:linear-gradient(90deg,#d6efec 0%,#f2faf9 55%,#ffffff 100%);box-shadow:0 2px 8px rgba(0,0,0,.05)}
.cat h3{position:absolute;left:26px;top:44px;font-size:19px;line-height:24px;font-weight:600;color:var(--teal-900)}
.cat .btn{position:absolute;left:26px;top:111px;width:90px;height:30px;line-height:30px;font-size:11px;text-align:center;border-radius:2px}
.btn-dark{background:var(--teal-900);color:var(--white)}
.cat .img{position:absolute;right:40px;top:20px;width:100px;height:150px;border-radius:10px}

.section-title{left:0;width:1200px;text-align:center;font-size:27px;font-weight:600;color:var(--teal-900)}
.product{top:1036px;width:205px}
.product .card{height:205px;background:var(--white);position:relative}
.product .img{position:absolute;left:30px;top:22px;width:145px;height:150px;border-radius:8px}
.tag{position:absolute;left:7px;top:7px;font-size:7px;color:var(--white);padding:3px 7px;border-radius:2px}
.product p{text-align:center;font-size:11.5px;line-height:16px;margin-top:9px}
.price{text-align:center;font-size:12px;margin-top:8px}
.price s{color:var(--grey-400);margin-right:16px}
.price b{font-weight:500;color:var(--teal-900)}
.cart-btn{position:absolute;left:48px;top:153px;width:110px;height:26px;line-height:26px;font-size:10px;text-align:center;border-radius:3px}

.blog{top:1563px;width:337px}
.blog .img{height:186px}
.blog .date{margin:14px 0 0 12px;display:flex;align-items:center;gap:8px;font-size:10px;color:var(--teal-900)}
.blog .date i{width:22px;height:22px;border-radius:50%;background:#7fc2bd;display:inline-block}
.blog p{margin:10px 0 0 12px;font-size:10.5px;line-height:17px;width:240px}

/* footer */
.footer{left:0;top:1955px;width:1200px;height:278px;background:var(--teal-800);color:#e0f0ee}
.foot-logo{left:157px;top:60px;font-size:32px;font-weight:600;color:#7fc8c1}
.foot-about{left:157px;top:113px;width:220px;font-size:10px;line-height:15px}
.foot-about a{color:#7fc8c1}
.foot-h{font-size:13px;font-weight:600;color:#7fc8c1}
.foot-list{font-size:10.5px;line-height:20px}
.foot-list .active{color:#7fc8c1;text-decoration:underline}
.contact{font-size:10.5px;line-height:15px;display:flex;gap:5px}
.email-in{left:777px;top:107px;width:266px;height:32px;border:1px solid #3f8a85;font-size:10.5px;padding:9px 11px;color:#a9d4cf}
.sub-btn{left:777px;top:148px;width:93px;height:31px;line-height:31px;background:#b7e0dc;color:var(--teal-900);font-size:11.5px;text-align:center;border-radius:2px}
.pay{left:551px;top:214px;display:flex;gap:17px;font-size:10.5px;font-weight:500;color:var(--white)}
.bottombar{left:0;top:2233px;width:1200px;height:32px;background:var(--teal-700);color:var(--white);font-size:10.5px;line-height:32px;padding-left:157px}
.social{position:absolute;right:157px;top:8px;display:flex;gap:8px}
.social i{width:17px;height:17px;border-radius:50%;background:#7fc8c1;display:block}
</style>
</head>
<body>
<div class="page">

  <div class="abs topbar">Welcome To Kaltir. <a>Read More</a>
    <div class="topbar-icons">
      <svg width="14" height="14" viewBox="0 0 14 14" fill="none" stroke="#9fd3ce" stroke-width="1.2"><circle cx="7" cy="4.5" r="2.7"/><path d="M2 13c0-3 2.3-4.8 5-4.8S12 10 12 13"/></svg>
      <svg width="15" height="14" viewBox="0 0 15 14" fill="none" stroke="#9fd3ce" stroke-width="1.2"><path d="M7.5 12.5 2 7a3 3 0 0 1 5.5-4 3 3 0 0 1 5.5 4z"/></svg>
      <svg width="18" height="14" viewBox="0 0 18 14" fill="none" stroke="#9fd3ce" stroke-width="1.2"><path d="M2 4h10v9H2zM4.5 4a2.5 2.5 0 0 1 5 0"/><text x="13" y="5" font-size="6" fill="#9fd3ce" stroke="none">0</text></svg>
    </div>
  </div>

  <section class="abs hero">
    <div class="abs logo">Kaltir</div>
    <nav class="abs nav"><span class="active">Home</span><span>Shop</span><span>About Us</span><span>Help</span><span>Blog</span></nav>
    <div class="abs search"><svg width="12" height="12" viewBox="0 0 12 12" fill="none" stroke="#0f6e69" stroke-width="1.2"><circle cx="7" cy="5" r="4"/><path d="M4 8 1 11"/></svg>search here</div>
    <div class="abs eyebrow">Get 10% Off</div>
    <h1 class="abs hero-title">Stride Air Walker Ankle<br>Fracture Boot</h1>
    <div class="abs btn-light hero-btn">Shop Now</div>
    <div class="abs hero-img" role="img" aria-label="Product photo of a tall grey walker boot beside a white air walker boot"></div>
    <div class="abs dots"><span></span><span></span><span class="on"></span><span></span></div>
  </section>

  <div class="abs feature" style="left:238px">
    <svg width="40" height="40" viewBox="0 0 40 40" fill="none" stroke="#0f6e69" stroke-width="1.6"><rect x="2" y="4" width="30" height="32"/><path d="M8 20h12M8 26h12M8 20v6"/><circle cx="32" cy="30" r="6" fill="#7fc2bd" stroke="none"/><path d="m29 30 2 2 4-4" stroke="#fff"/></svg>
    <div><b>Free Shipping</b>On Orders Over $50</div>
  </div>
  <div class="abs feature" style="left:506px">
    <svg width="40" height="40" viewBox="0 0 40 40" fill="none" stroke="#0f6e69" stroke-width="1.6"><path d="M20 2l4 4 6-1 1 6 5 3-3 6 3 6-5 3-1 6-6-1-4 4-4-4-6 1-1-6-5-3 3-6-3-6 5-3 1-6 6 1z"/><circle cx="20" cy="20" r="9" fill="#bfe6e2" stroke="none"/><path d="m16 24 8-8"/><circle cx="16.5" cy="16.5" r="1.5"/><circle cx="23.5" cy="23.5" r="1.5"/></svg>
    <div><b>Official Discounts</b>Save Big On Next Product</div>
  </div>
  <div class="abs feature" style="left:804px">
    <svg width="40" height="40" viewBox="0 0 40 40" fill="none" stroke="#0f6e69" stroke-width="1.6"><circle cx="20" cy="20" r="17"/><circle cx="20" cy="20" r="11" stroke="#7fc2bd" stroke-width="4"/><circle cx="20" cy="20" r="8"/></svg>
    <div><b>24/7 Helpline</b>Care Till The End</div>
  </div>

  <div class="abs band"></div>

  <div class="abs cat" style="left:244px">
    <h3>Fracture<br>Walker Boot</h3>
    <div class="btn btn-dark">View All</div>
    <div class="img" role="img" aria-label="Photo of a black walker boot" style="background:linear-gradient(180deg,#5a6061,#2d3233)"></div>
  </div>
  <div class="abs cat" style="left:611px">
    <h3>Brace (Ankle)<br>Products</h3>
    <div class="btn btn-light">View All</div>
    <div class="img" role="img" aria-label="Photo of a foot wearing a black ankle brace" style="background:linear-gradient(180deg,#a0735a,#1f2223 55%)"></div>
  </div>

  <h2 class="abs section-title" style="top:978px">Our Products</h2>

  <div class="abs product" style="left:157px">
    <div class="card"><span class="tag" style="background:var(--sale)">SALE</span><div class="img" role="img" aria-label="Photo of black ankle support wraps" style="background:linear-gradient(135deg,#e9e2dc,#2a2d2e)"></div></div>
    <p>Lorem Ipsum Is Dummy<br>Printing Industry.</p>
    <div class="price"><s>$540.00</s><b>$498.00</b></div>
  </div>
  <div class="abs product" style="left:383px">
    <div class="card"><span class="tag" style="background:var(--sold)">SOLD</span><div class="img" role="img" aria-label="Photo of a grey walker boot with teal accents" style="background:linear-gradient(160deg,#8b9293,#4d5657)"></div></div>
    <p>Lorem Ipsum Is Dummy<br>Printing Industry.</p>
    <div class="price"><s>$540.00</s><b>$498.00</b></div>
  </div>
  <div class="abs product" style="left:609px">
    <div class="card"><div class="img" role="img" aria-label="Photo of compression ankle sleeves" style="background:linear-gradient(160deg,#eef0f0,#c4c9c8)"></div><div class="cart-btn btn-dark">Add To Cart</div></div>
    <p>Lorem Ipsum Is Dummy<br>Printing Industry.</p>
    <div class="price"><s>$540.00</s><b>$498.00</b></div>
  </div>
  <div class="abs product" style="left:836px">
    <div class="card"><span class="tag" style="background:var(--sale)">SALE</span><div class="img" role="img" aria-label="Photo of a white air walker boot" style="background:linear-gradient(160deg,#dcdde2,#b9bbc5 70%,#5fd0cf)"></div></div>
    <p>Lorem Ipsum Is Dummy<br>Printing Industry.</p>
    <div class="price"><s>$540.00</s><b>$498.00</b></div>
  </div>

  <div class="abs btn-dark" style="left:555px;top:1325px;width:90px;height:31px;line-height:31px;font-size:11px;text-align:center;border-radius:2px">View All</div>

  <h2 class="abs section-title" style="top:1506px">Our Blogs</h2>

  <div class="abs blog" style="left:251px">
    <div class="img" role="img" aria-label="Photo of a walker using a crutch and an ankle boot outdoors" style="background:linear-gradient(160deg,#8fa9a3,#4d6d83 60%,#a7b3b0)"></div>
    <div class="date"><i></i>Oct 18, 2024</div>
    <p>Lorem Ipsum Is Simply Dummy Text Of The Printing And Typesetting Industry...</p>
  </div>
  <div class="abs blog" style="left:612px">
    <div class="img" role="img" aria-label="Photo of a foot wrapped in a blue cold compress" style="background:linear-gradient(160deg,#6f8e9a,#3a82c4 55%,#9bb6bf)"></div>
    <div class="date"><i></i>Oct 18, 2024</div>
    <p>Lorem Ipsum Is Simply Dummy Text Of The Printing And Typesetting Industry...</p>
  </div>

  <div class="abs btn-light" style="left:553px;top:1853px;width:94px;height:34px;line-height:34px;border:1px solid #e6e8e8">View All</div>

  <footer class="abs footer">
    <div class="abs foot-logo">Kaltir</div>
    <p class="abs foot-about">Lorem Ipsum Is Simply Dummy Text Of The Printing And Typesetting Industry. Lorem Ipsum Has Been The Industry's Standard Dummy Text Ever... <a>About Us</a></p>

    <div class="abs foot-h" style="left:431px;top:56px">Contact Us</div>
    <div class="abs contact" style="left:431px;top:87px"><svg width="10" height="12" viewBox="0 0 10 12" fill="none" stroke="#e0f0ee" stroke-width="1.1"><path d="M2 1l2 3-1 1.5c.8 1.7 2 2.9 3.5 3.5L8 8l2 2-1.5 1.5C4.5 11 0 6 1 2z"/></svg>555-210-4471</div>
    <div class="abs contact" style="left:431px;top:118px"><svg width="11" height="10" viewBox="0 0 11 10" fill="none" stroke="#e0f0ee" stroke-width="1.1"><rect x=".5" y="1" width="10" height="8"/><path d="m.5 1 5 4 5-4"/></svg>info@kaltir.com</div>
    <div class="abs contact" style="left:431px;top:150px"><svg width="10" height="12" viewBox="0 0 10 12" fill="none" stroke="#e0f0ee" stroke-width="1.1"><path d="M5 11S1 7 1 4.5a4 4 0 0 1 8 0C9 7 5 11 5 11z"/><circle cx="5" cy="4.5" r="1.4"/></svg><span>14 Harbour Lane, #03-12,<br>Marlow 204517</span></div>

    <div class="abs foot-h" style="left:637px;top:56px">Quick Links</div>
    <div class="abs foot-list" style="left:637px;top:82px"><div class="active">Home</div><div>Shop</div><div>About Us</div><div>Help</div><div>Blog</div></div>

    <svg class="abs" style="left:777px;top:54px" width="36" height="36" viewBox="0 0 36 36" fill="none" stroke="#e0f0ee" stroke-width="1.3"><path d="M2 14v20h32V14L18 3z"/><path d="m2 34 13-11h6l13 11M2 14l12 9M34 14l-12 9"/><rect x="9" y="7" width="18" height="13"/><circle cx="18" cy="13" r="3"/></svg>
    <div class="abs foot-h" style="left:822px;top:57px">Sign Up And Save!</div>
    <div class="abs" style="left:822px;top:75px;font-size:9.5px">Exclusive Email Offers &amp; Limited Time</div>
    <div class="abs email-in">Enter Email</div>
    <div class="abs sub-btn">Subscribe</div>

    <div class="abs foot-h" style="left:431px;top:212px">We Accept</div>
    <div class="abs pay"><span>Paylo</span><span>Crestcard</span><span>Tapwell</span><span>Orbit Pay</span><span>Duocard</span><span>Norpay</span><span>Swiftpay</span></div>
  </footer>

  <div class="abs bottombar">© 2024 Kaltir. All Right Reserved
    <div class="social"><i></i><i></i><i></i></div>
  </div>

</div>
</body>
</html>
```